Business Card Design Project

We need a buisness card for a new digital sinage company. Our target cliants are small to mediaum buisness who want to advertise on out digital sinage network

Target Market(s)

Small to medium buisness

Industry/Entity Type

Digital

Requirements
Must have
• Must have logo

```html
<!DOCTYPE html>
<html lang="en">
<head>
<meta charset="utf-8">
<title>Vizo – Business Card</title>
<link rel="stylesheet" href="https://fonts.googleapis.com/css2?family=Lato:wght@400;700;900&display=swap">
<style>
  :root {
    --page-bg: #e6e9ec;
    --card-white: #ffffff;
    --brand-blue: #1f78c8;
    --brand-blue-dark: #1456a8;
    --brand-blue-light: #3a9be0;
    --brand-orange: #f39c12;
    --text-dark: #2b2b2b;
    --text-mid: #3d3d3d;
  }
  * { margin: 0; padding: 0; box-sizing: border-box; }
  html, body {
    width: 1200px;
    height: 960px;
    overflow: hidden;
    background: var(--page-bg);
    font-family: "Lato", Arial, sans-serif;
  }
  .sheet {
    width: 1200px;
    height: 960px;
    display: flex;
    flex-direction: column;
    align-items: center;
    justify-content: center;
    gap: 50px;
  }
  .card {
    width: 700px;
    height: 400px;
    position: relative;
    box-shadow: 0 6px 18px rgba(0,0,0,0.15);
  }

  /* Front */
  .card-front { background: var(--card-white); }
  .front-brand {
    position: absolute;
    left: 90px;
    top: 150px;
    display: flex;
    align-items: center;
    gap: 14px;
  }
  .front-brand .brand-square {
    width: 34px;
    height: 34px;
    background: var(--brand-blue);
  }
  .front-brand .brand-name {
    font-weight: 900;
    font-size: 52px;
    color: var(--brand-blue);
    line-height: 1;
  }
  .contact {
    position: absolute;
    left: 380px;
    top: 82px;
    color: var(--text-mid);
    font-size: 18px;
    line-height: 1.4;
  }
  .contact-list { list-style: none; }
  .contact-list li { display: flex; gap: 12px; }
  .contact-list .label { color: var(--brand-blue); width: 10px; }
  .contact-web {
    font-weight: 700;
    color: var(--text-dark);
    margin-top: 20px;
  }
  .contact-address { margin-top: 18px; }
  .person {
    position: absolute;
    left: 380px;
    bottom: 44px;
  }
  .person-name {
    color: var(--brand-blue);
    font-size: 26px;
    letter-spacing: 0.5px;
    text-transform: uppercase;
    line-height: 1.15;
  }
  .person-title {
    color: var(--text-dark);
    font-size: 18px;
    text-transform: uppercase;
  }
  .corner-mark {
    position: absolute;
    right: 0;
    bottom: 50px;
    width: 54px;
    height: 54px;
    background: var(--brand-blue);
  }

  /* Back */
  .card-back {
    background: linear-gradient(100deg, var(--brand-blue-dark) 0%, var(--brand-blue) 55%, var(--brand-blue-light) 100%);
    display: flex;
    align-items: center;
    justify-content: center;
  }
  .back-brand {
    display: flex;
    align-items: center;
    gap: 22px;
  }
  .back-brand .brand-square {
    width: 70px;
    height: 70px;
    background: var(--brand-orange);
  }
  .back-brand .brand-name {
    font-weight: 900;
    font-size: 88px;
    color: var(--card-white);
    line-height: 1;
  }
</style>
</head>
<body>
  <main class="sheet">
    <section class="card card-front" aria-label="Business card front">
      <div class="front-brand">
        <span class="brand-square"></span>
        <span class="brand-name">Vizo</span>
      </div>
      <div class="contact">
        <ul class="contact-list">
          <li><span class="label">t</span><span>(555) 24 610 38 42</span></li>
          <li><span class="label">f</span><span>(555) 71 482 90 16</span></li>
          <li><span class="label">e</span><span>name@vizodisplay.com</span></li>
        </ul>
        <p class="contact-web">www.vizodisplay.com</p>
        <p class="contact-address">Rue des Palmiers - Mermoz<br>BP 218 - City, Country</p>
      </div>
      <div class="person">
        <p class="person-name">Lena Marchetti</p>
        <p class="person-title">Operation Manager</p>
      </div>
      <span class="corner-mark"></span>
    </section>

    <section class="card card-back" aria-label="Business card back">
      <div class="back-brand">
        <span class="brand-square"></span>
        <span class="brand-name">Vizo</span>
      </div>
    </section>
  </main>
</body>
</html>
```